Business Card Design

We need a business card design for a new company based in Allen, Texas. (outside of Dallas,Texas) We offer Business Management Solutions to Entrepreneurs, as well as Corporate Businesses. Our product line offers solutions to Image, Branding, Social Media marketing, business development strategies, banking / funding solutions, just to name a few. We would like to see designs that convey strength and confidence. I have attached a sample design of our company name. Designers you may use company name as either: Tovan or Tovan Corporation, depending on the design layout.

Please show alternate color of Black as well.

Industry/Entity Type

Business

Contact Information for Business Card

Tovan Corporation

4862 N. Brisbury Lane, STE 300
Kessler, TX 75284
Office: 512.638.4471
Fax: 512.638.4472

Dr. Louis Brennick
Business Development Director

```html
<!DOCTYPE html>
<html lang="en">
<head>
<meta charset="utf-8">
<title>Tovan Corporation – Business Card</title>
<link rel="stylesheet" href="https://fonts.googleapis.com/css2?family=PT+Sans&family=PT+Sans+Narrow&display=swap">
<style>
  :root {
    --page-bg: #f2f2f4;
    --card-black: #070707;
    --brand-blue: #0071bb;
    --text-white: #ffffff;
  }
  * { margin: 0; padding: 0; box-sizing: border-box; }
  html, body {
    width: 1200px;
    height: 1000px;
    overflow: hidden;
    background: var(--page-bg);
  }
  .card-sheet {
    position: relative;
    width: 1200px;
    height: 1000px;
  }
  .card {
    position: absolute;
    left: 236px;
    width: 729px;
    height: 415px;
    background: var(--card-black);
    overflow: hidden;
  }
  .card--front { top: 115px; }
  .card--back  { top: 533px; }

  .stripe-band {
    position: absolute;
    top: 0;
    height: 100%;
    background: var(--brand-blue);
  }
  .stripe-band__rule {
    position: absolute;
    top: 0;
    height: 100%;
    width: 7px;
    background: var(--card-black);
  }
  .card--front .stripe-band { left: 565px; width: 164px; }
  .card--front .stripe-band__rule { left: 53px; }
  .card--back .stripe-band { left: 0; width: 164px; }
  .card--back .stripe-band__rule { left: 104px; width: 6px; }

  .text {
    position: absolute;
    color: var(--text-white);
    line-height: 1;
    white-space: nowrap;
  }
  .brand-name {
    left: 52px;
    top: 303px;
    font-family: "PT Sans", sans-serif;
    font-size: 52px;
    letter-spacing: 0.6px;
  }
  .brand-tagline {
    left: 52px;
    top: 367px;
    font-family: "PT Sans Narrow", sans-serif;
    font-size: 23px;
  }
  .contact-name {
    left: 181px;
    top: 153px;
    font-family: "PT Sans", sans-serif;
    font-size: 30px;
  }
  .contact-title {
    left: 181px;
    top: 200px;
    font-family: "PT Sans Narrow", sans-serif;
    font-size: 23px;
  }
  .contact-details {
    left: 181px;
    top: 248px;
    font-family: "PT Sans Narrow", sans-serif;
    font-size: 30px;
    line-height: 42.5px;
    font-style: normal;
  }
</style>
</head>
<body>
  <main class="card-sheet">
    <section class="card card--front" aria-label="Card front">
      <div class="stripe-band"><div class="stripe-band__rule"></div></div>
      <div class="text brand-name">tovan corporation</div>
      <div class="text brand-tagline">Business Management Solutions</div>
    </section>

    <section class="card card--back" aria-label="Card back">
      <div class="stripe-band"><div class="stripe-band__rule"></div></div>
      <div class="text contact-name">Dr. Louis Brennick</div>
      <div class="text contact-title">Business Development Director</div>
      <address class="text contact-details">
        4862 N. Brisbury Lane<br>
        STE 300 Kessler, TX 75284<br>
        Office: 512.638.4471 Fax: 512.638.4472
      </address>
    </section>
  </main>
</body>
</html>
```